logo for security & safety training, education consultants
Marlow Advisory Nest Pte Ltd
Professional
LTC (RET) LIM BOON KEAT ROBERT MBA
DIRECTOR
47 JALAN TEMBUSIRA SINGAPORE 528806
robert@marlownest-example.com
www.marlownest-example.com
Perhaps some iso logo and same award logo in dummies

```html
<!DOCTYPE html>
<html lang="en">
<head>
<meta charset="utf-8">
<title>Marlow Advisory Nest – Business Card</title>
<link href="https://fonts.googleapis.com/css2?family=Open+Sans:wght@400;600;800&display=swap" rel="stylesheet">
<style>
  :root {
    --page-bg: #e9e6e1;
    --card-white: #ffffff;
    --brand-blue: #2a14f0;
    --logo-blue: #1f2f8f;
    --band-black: #0d0d0f;
    --text-white: #ffffff;
    --icon-dark: #1a1a1a;
  }
  * { margin: 0; padding: 0; box-sizing: border-box; }
  html, body {
    width: 1200px; height: 902px; overflow: hidden;
    background: var(--page-bg);
    font-family: "Open Sans", Arial, sans-serif;
  }
  .business-card {
    position: absolute; left: 100px; top: 166px;
    width: 1000px; height: 570px;
    background: var(--card-white);
    overflow: hidden;
    box-shadow: 0 10px 30px rgba(0,0,0,0.18);
  }
  .card-shapes { position: absolute; inset: 0; }
  .brand-mark {
    position: absolute; left: 70px; top: 120px;
    display: flex; align-items: center; gap: 14px;
  }
  .brand-mark .mark-dot {
    width: 34px; height: 34px; border-radius: 50%;
    background: var(--logo-blue);
  }
  .brand-mark .brand-name {
    font-weight: 800; font-size: 60px; letter-spacing: 1px;
    color: var(--logo-blue); line-height: 1;
  }
  .person {
    position: absolute; right: 70px; top: 286px;
    text-align: right; color: var(--text-white);
  }
  .person .person-name { font-weight: 600; font-size: 17px; letter-spacing: 0.3px; }
  .person .person-title { font-weight: 400; font-size: 12px; letter-spacing: 1px; margin-top: 4px; margin-right: 70px; }
  .contact-list {
    position: absolute; left: 20px; top: 368px;
    list-style: none; color: var(--text-white);
    font-size: 13px; line-height: 22px;
  }
  .contact-list li { display: flex; align-items: center; gap: 7px; }
  .contact-list svg { width: 14px; height: 14px; flex: none; }
  .web-strip {
    position: absolute; right: 60px; top: 432px;
    color: var(--text-white); font-size: 19px; letter-spacing: 3px;
  }
</style>
</head>
<body>
  <div class="business-card">
    <svg class="card-shapes" viewBox="0 0 1000 570" width="1000" height="570" aria-hidden="true">
      <polygon points="0,258 740,258 760,278 780,258 1000,258 1000,254 780,254 760,274 740,254 0,254" fill="var(--band-black)"/>
      <polygon points="0,262 742,262 760,280 778,262 1000,262 1000,520 0,520" fill="var(--brand-blue)"/>
      <polygon points="742,258 778,258 760,278" fill="var(--band-black)"/>
      <polygon points="600,422 1000,422 1000,482 560,482" fill="var(--band-black)"/>
      <rect x="0" y="520" width="1000" height="6" fill="var(--band-black)"/>
    </svg>

    <div class="brand-mark">
      <span class="mark-dot"></span>
      <span class="brand-name">MARLOW</span>
    </div>

    <div class="person">
      <p class="person-name">LTC (RET) LIM BOON KEAT ROBERT MBA</p>
      <p class="person-title">DIRECTOR</p>
    </div>

    <ul class="contact-list">
      <li><svg viewBox="0 0 14 14"><circle cx="7" cy="7" r="7" fill="#fff"/><path d="M7 3a2.5 2.5 0 0 0-2.5 2.5C4.5 8 7 11 7 11s2.5-3 2.5-5.5A2.5 2.5 0 0 0 7 3z" fill="var(--icon-dark)"/></svg>47 JALAN TEMBUSIRA<br></li>
      <li style="padding-left:21px">SINGAPORE 528806</li>
      <li><svg viewBox="0 0 14 14"><circle cx="7" cy="7" r="7" fill="#fff"/><path d="M4.5 3.5l1.5 0 .7 2-1 .8a5 5 0 0 0 2.5 2.5l.8-1 2 .7v1.5c-3.5.5-7-3-6.5-6.5z" fill="var(--icon-dark)"/></svg>+65 6480 3127</li>
      <li><svg viewBox="0 0 14 14"><circle cx="7" cy="7" r="7" fill="#fff"/><rect x="5" y="3" width="4" height="8" rx="0.8" fill="var(--icon-dark)"/></svg>+65 9407 5512</li>
      <li><svg viewBox="0 0 14 14"><circle cx="7" cy="7" r="7" fill="#fff"/><rect x="3.5" y="5.5" width="7" height="4" fill="var(--icon-dark)"/><rect x="5" y="3.5" width="4" height="2" fill="var(--icon-dark)"/></svg>+65 6480 3128</li>
      <li><svg viewBox="0 0 14 14"><circle cx="7" cy="7" r="7" fill="#fff"/><rect x="3.5" y="4.5" width="7" height="5" fill="var(--icon-dark)"/><path d="M3.5 4.5L7 7.5l3.5-3" stroke="#fff" stroke-width="0.8" fill="none"/></svg>robert@marlownest-example.com</li>
      <li><svg viewBox="0 0 14 14"><circle cx="7" cy="7" r="7" fill="#fff"/><circle cx="7" cy="7" r="3.5" stroke="var(--icon-dark)" stroke-width="1" fill="none"/><path d="M3.5 7h7M7 3.5v7" stroke="var(--icon-dark)" stroke-width="0.8"/></svg>www.marlownest-example.com</li>
    </ul>

    <p class="web-strip">www.marlownest-example.com</p>
  </div>
</body>
</html>
```